Web Design for online C2C site

We need a web design for a brand new website that has users logging into an account and uploading pictures of goods and services that they want to trade.
We like 'fresh' and simple websites that have a white background, with easy navigation, a splash of colour (grey, blue, and green is a colour scheme that appeals to us) but doesn't look overly boring.
The site needs a modern look for an old type of trade - a barter system.
We have attached a file with our logo and would like to use the top logo from the file (grey, green, and blue)
Updates
Project Deadline Extended
Reason: The timeline has been extended until this Sunday, December 2nd for all who require extra time to design a web layout.
Cheers,
Marisol
Industry/Entity Type
Trade
Look and feel
Each slider illustrates characteristics of the customer's brand and the style your logo design should communicate.

```html
<!DOCTYPE html>
<html lang="en">
<head>
<meta charset="utf-8">
<title>TradeNest</title>
<link rel="stylesheet" href="https://fonts.googleapis.com/css2?family=Didact+Gothic&family=PT+Sans:wght@400;700&family=Noto+Serif:wght@400;700&display=swap">
<style>
  :root {
    --ink: #3d4142;
    --nav-bg: #3f4546;
    --nav-text: #f2f2f2;
    --header-top: #ffffff;
    --header-bg: #eeeff1;
    --brand-blue: #5b7fc4;
    --brand-green: #4cb51b;
    --green-light: #6fcf24;
    --green-dark: #3f9e12;
    --button-ink: #14315d;
    --card-top: #e6e7e9;
    --card-bottom: #f8f8f9;
    --footer-bg: #f2f2f4;
    --footer-line: #e1e2e4;
    --rule: #d6d7d9;
    --muted: #555a5c;
    --icon: #1c1c1c;
  }
  * { box-sizing: border-box; margin: 0; padding: 0; }
  html, body { width: 1200px; height: 1029px; overflow: hidden; background: #fff; }
  body { position: relative; font-family: "PT Sans", sans-serif; color: var(--ink); }

  .site-header {
    position: absolute; left: 0; top: 29px; width: 1200px; height: 172px;
    background: linear-gradient(#f7f7f8, var(--header-bg));
    border-top: 1px solid #e8e8ea;
  }
  .brand {
    position: absolute; left: 462px; top: 52px; display: flex; align-items: center; gap: 10px;
  }
  .brand-mark { width: 60px; height: 60px; border-radius: 50%; background: var(--brand-blue); }
  .brand-name { font-family: "PT Sans", sans-serif; font-weight: 700; font-size: 34px; color: var(--brand-blue); }
  .tagline {
    position: absolute; left: 0; top: 134px; width: 1189px; text-align: center;
    font-family: "Didact Gothic", sans-serif; font-size: 26px; letter-spacing: 1px; color: var(--ink);
  }

  .member-login {
    position: absolute; left: 884px; top: 0; width: 139px; height: 114px; background: #dfe0e1;
    padding: 4px 8px 0 13px;
  }
  .member-login h2 { font-weight: 400; font-size: 14.5px; color: var(--ink); display: flex; justify-content: space-between; align-items: center; }
  .member-login .field {
    display: block; width: 107px; height: 20px; margin-top: 5px; margin-left: 5px;
    background: #fff; border: 1px solid #cfd0d2; font-size: 12px; color: var(--brand-green); padding: 2px 14px;
  }
  .member-login .login-btn {
    position: absolute; right: 12px; top: 87px; width: 66px; height: 20px; border-radius: 10px;
    background: linear-gradient(#f0f0f0, #bdbdbd); border: 1px solid #a9a9a9; font-size: 11px; text-align: center; line-height: 18px; color: #333;
  }

  .main-nav {
    position: absolute; left: 0; top: 201px; width: 1200px; height: 44px; background: var(--nav-bg);
    font-family: "Didact Gothic", sans-serif; font-size: 15.5px; color: var(--nav-text); text-transform: uppercase;
  }
  .main-nav span { position: absolute; top: 12px; transform: translateX(-50%); white-space: nowrap; }

  .step-card {
    position: absolute; top: 316px; width: 253px; height: 208px;
    background: linear-gradient(var(--card-top), var(--card-bottom) 60%, #f1f1f2);
    box-shadow: 0 8px 10px -6px rgba(0,0,0,0.25);
    text-align: center; font-family: "Didact Gothic", sans-serif; font-size: 21px; color: var(--ink); line-height: 1.05;
  }
  .step-card h3 { font-weight: 400; font-size: 21px; position: absolute; left: 0; width: 100%; }
  .step-icon { position: absolute; left: 50%; transform: translateX(-50%); }

  .signup {
    position: absolute; left: 477px; top: 579px; width: 240px; height: 52px; border-radius: 4px;
    background: linear-gradient(var(--green-light), var(--green-dark));
    box-shadow: 0 5px 0 #2b2f31;
    font-weight: 700; font-size: 25px; color: var(--button-ink); text-align: center; line-height: 50px;
  }

  .welcome {
    position: absolute; left: 194px; top: 686px; width: 816px;
    display: flex; align-items: center; gap: 16px;
  }
  .welcome::before, .welcome::after { content: ""; flex: 1; height: 1px; background: var(--rule); }
  .welcome h1 { font-family: "Noto Serif", serif; font-weight: 700; font-size: 18px; color: #4a4d4e; letter-spacing: .3px; }
  .welcome-text {
    position: absolute; left: 0; top: 725px; width: 1200px; text-align: center;
    font-family: "Noto Serif", serif; font-size: 14.5px; line-height: 22px; color: #4a4d4e; letter-spacing: .2px;
  }

  .site-footer {
    position: absolute; left: 0; top: 833px; width: 1200px; height: 196px; background: var(--footer-bg);
    border-top: 1px solid var(--footer-line);
  }
  .footer-nav { position: absolute; left: 183px; top: 22px; display: flex; font-size: 12px; color: #222; }
  .footer-nav span { padding: 0 13px; border-left: 1px solid #999; line-height: 12px; }
  .footer-nav span:first-child { border-left: 0; padding-left: 0; padding-right: 15px; }
  .social { position: absolute; left: 901px; top: 19px; display: flex; gap: 10px; }
  .social i { width: 22px; height: 22px; border-radius: 50%; background: #55595b; display: block; }
  .footer-col { position: absolute; top: 81px; font-size: 10px; color: var(--muted); }
  .footer-col h4 { font-weight: 400; font-size: 13.5px; color: var(--green-dark); margin-bottom: 6px; }
  .footer-col p { line-height: 12.5px; letter-spacing: .3px; padding-left: 2px; }
  .footer-col .contact-line { line-height: 20px; }
  .footer-brand { position: absolute; left: 183px; top: 163px; display: flex; align-items: center; gap: 4px; font-size: 11px; font-weight: 700; color: #555; }
  .footer-brand i { width: 20px; height: 20px; border-radius: 50%; background: #707476; display: block; }
  .copyright { position: absolute; right: 207px; top: 171px; font-size: 10px; color: #222; }
</style>
</head>
<body>

<header class="site-header">
  <div class="brand">
    <span class="brand-mark"></span>
    <span class="brand-name">TradeNest</span>
  </div>
  <p class="tagline">LOREM IPSUM DOLOR SIT AMET</p>
</header>

<form class="member-login">
  <h2>Members Login
    <svg width="11" height="11" viewBox="0 0 11 11"><circle cx="5.5" cy="5.5" r="4.5" fill="none" stroke="#222" stroke-width="1.5"/><line x1="3" y1="8" x2="8" y2="3" stroke="#222" stroke-width="1.5"/></svg>
  </h2>
  <span class="field">user</span>
  <span class="field">···········</span>
  <span class="login-btn">Login</span>
</form>

<nav class="main-nav">
  <span style="left:257px">About us</span>
  <span style="left:389px">For businesses</span>
  <span style="left:548px;top:10px">For individuals</span>
  <span style="left:696px;top:10px">Housing swaps</span>
  <span style="left:842px">Sponsors</span>
  <span style="left:963px;top:10px">Blog</span>
</nav>

<section class="step-card" style="left:204px">
  <h3 style="top:45px">Up your pictures</h3>
  <div class="step-icon" role="img" aria-label="Camera with upload arrow icon" style="top:95px;width:56px;height:66px;">
    <svg width="56" height="66" viewBox="0 0 56 66"><path d="M18 0 L28 12 H22 V20 H14 V12 H8 Z" fill="var(--icon)"/><rect x="0" y="24" width="56" height="42" rx="6" fill="var(--icon)"/><circle cx="40" cy="45" r="10" fill="none" stroke="#fff" stroke-width="4"/><rect x="7" y="40" width="8" height="4" fill="#fff"/></svg>
  </div>
</section>

<section class="step-card" style="left:476px">
  <h3 style="top:34px">Publish your goods<br>or services</h3>
  <div class="step-icon" role="img" aria-label="Connected people network icon" style="top:100px;width:70px;height:60px;">
    <svg width="70" height="60" viewBox="0 0 70 60"><g fill="none" stroke="var(--icon)" stroke-width="4"><line x1="35" y1="10" x2="35" y2="58"/><line x1="6" y1="30" x2="35" y2="50"/><line x1="64" y1="30" x2="35" y2="50"/><line x1="6" y1="30" x2="64" y2="30"/></g><g fill="var(--icon)"><circle cx="35" cy="8" r="6"/><circle cx="6" cy="30" r="6"/><circle cx="64" cy="30" r="6"/><circle cx="35" cy="50" r="7"/></g></svg>
  </div>
</section>

<section class="step-card" style="left:747px">
  <h3 style="top:41px">Make a trade</h3>
  <div class="step-icon" role="img" aria-label="Handshake icon" style="top:91px;width:80px;height:62px;background:linear-gradient(#2a2a2a,#111);border-radius:40%;"></div>
</section>

<div class="signup">SIGN UP NOW</div>

<div class="welcome"><h1>WELCOME TO TRADENEST</h1></div>
<p class="welcome-text">Aenean lacinia, urna non tristique dictum, mi diam feugiat libero, quis commodo magna eros sit amet diam.<br>Maecenas commodo lectus at turpis rutrum consectetur mattis nunc consequat.</p>

<footer class="site-footer">
  <nav class="footer-nav">
    <span>About us</span><span>For Businesses</span><span>For Individuals</span><span>Housing swaps</span><span>Sponsor</span><span>Blog</span>
  </nav>
  <div class="social"><i></i><i></i><i></i></div>

  <div class="footer-col" style="left:183px">
    <h4>Higlights</h4>
    <p>Lorem ipsum dolor sit amet, consectetur .<br>Donec sed nunc at leo posuere ornare.<br>Praesent et urna in mi faucibus auctor.</p>
  </div>
  <div class="footer-col" style="left:512px">
    <h4>Latest News</h4>
    <p>Lorem ipsum dolor sit amet, consectetur .<br>Donec sed nunc at leo posuere ornare.<br>Praesent et urna in mi faucibus auctor.</p>
  </div>
  <div class="footer-col" style="left:828px">
    <h4>Contact</h4>
    <p class="contact-line">Ph: +(10) <b>555 0142 880</b><br>Email: hello@tradenest.example</p>
  </div>

  <div class="footer-brand"><i></i>TradeNest</div>
  <p class="copyright">2012 © All rights reserved</p>
</footer>

</body>
</html>
```